Tessaro Lane Website

We are starting a marketing company and to do that we need a website! We want a website that will inspire and persuade to bring out the awesomeness in our clients.
What we want to see:
- Inspirational and persuasive imagery that relate to Branding.
- No cliche images eg. business man, suits and hand shakes
- We want to transform and educate our clients.
- We want to show them the path and would like our website to really act as a guide that guides them step by step through our process.
- We want the portray that we are an investment but not have a pretentious way to it. We put our heart into every project and that is how we treat our clients.
-When you submit your design please include what platform you have created for. Preference would be Wordpress or Joobla.

We have included the psd file for the wire frame, logo files, font files, site map and a link to a video we create to give you more information on what we would like to see. http://clipvault-demo.example/t/qx903LmaP

Feel free to make small modification to the logos if you think it will improve it. Your creativity and advice is most welcome.

One thing we forgot. We would like to have our contact information near the top of the website as well as at the bottom.  Here is out contact info:

Email: info@tessarolane.ca
Phone: 555-013-4829

Reason: As we are new with the platform and that we want to optimize our results, we decided to extend the deadline by 15 days. Thanks!

Target Market(s)

28-60, Male and Female, Oil field, Local Businesses, Dentists, Chiropractors, Hair salon, Construction/Renovation, Events etc

Industry/Entity Type

Investment

Requirements
Must have
• - 4 Inspirational and persuasive Imagery for the top portion of the website
- Must have a feel as if your not on a website an example of this is linked below.
http://www.pitchgallery-demo.example/design/482907/web-design-by-dalia-fenwick
Nice to have
• - Creative advice from you.
- Creative buttons for Get Free Quote and Subscribe buttons. Something out of the box that draws peoples attention. eg. a 'B' button. Just and example but still something related to branding.
Should not have
• No Cliches

```html
<!DOCTYPE html>
<html lang="en">
<head>
<meta charset="utf-8">
<title>Tessaro Lane</title>
<link href="https://fonts.googleapis.com/css2?family=Signika:wght@400;600;700&family=PT+Sans:ital,wght@0,400;0,700;1,700&display=swap" rel="stylesheet">
<style>
:root{
  --page:#f7f7f7;
  --dark:#4a4a4a;
  --ink:#505050;
  --green:#5b7f35;
  --lime:#a4c43e;
  --lime-light:#b6d34f;
  --lime-text:#8db52a;
  --head-green:#4f7a29;
  --panel:#e4e4e4;
  --white:#ffffff;
  --callout:#52c943;
}
*{box-sizing:border-box;margin:0;padding:0}
html,body{width:1200px;height:981px;overflow:hidden}
body{background:var(--page);font-family:"PT Sans",sans-serif;color:var(--ink);position:relative}
.topbar{position:absolute;left:0;top:0;width:1200px;height:13px;background:var(--dark)}
.abs{position:absolute}

.logo{left:130px;top:24px;width:225px;display:flex;align-items:center;gap:12px}
.logo-mark{flex:none;width:44px;height:44px;background:var(--lime);border-radius:50%}
.logo-name{font-family:"Signika",sans-serif;font-weight:700;font-size:29px;color:#7a7a7a;line-height:28px;letter-spacing:.5px}
.tagline{left:130px;top:90px;width:236px;text-align:center;font-style:italic;font-weight:700;font-size:15px;color:#5a5a5a}

.nav{left:370px;top:24px;display:flex;gap:15px}
.nav-tab{width:164px;height:44px;border-radius:4px;background:linear-gradient(#bcbcbc,#999);color:var(--white);font-family:"Signika",sans-serif;font-weight:700;font-size:18px;display:flex;align-items:center;justify-content:center;text-shadow:0 1px 1px rgba(0,0,0,.35);position:relative}
.nav-tab.active{background:linear-gradient(#6f9a3a,#a4c43e)}
.nav-tab.active::after{content:"";position:absolute;left:72px;bottom:-10px;border:10px solid transparent;border-bottom:0;border-top-color:var(--lime)}

.side-menu{left:130px;top:142px;width:220px;height:259px;background:var(--green);border-radius:4px;list-style:none;padding-top:5px}
.side-menu li{height:50px;padding-left:44px;display:flex;align-items:center;font-family:"Signika",sans-serif;font-weight:700;font-size:15px;color:var(--white);letter-spacing:.5px;position:relative}
.side-menu li.current::before{content:"";position:absolute;left:18px;width:9px;height:9px;border-radius:50%;background:var(--lime-light)}

.hero{left:370px;top:82px;width:700px;height:319px;border-radius:4px;overflow:hidden;border-bottom:3px solid #333}
.hero-art{position:absolute;inset:0;background:linear-gradient(90deg,#f4f4f4 0%,#e9eef3 50%,#ececec 100%)}
.callout{position:absolute;left:430px;top:205px;width:270px;height:111px;background:var(--callout);color:var(--white);padding:14px 14px}
.callout h2{font-family:"PT Sans",sans-serif;font-weight:700;font-size:21px;line-height:21px;max-width:205px}
.callout p{font-weight:700;font-size:14px;line-height:14px;margin-top:10px;max-width:235px}

.connect{left:130px;top:422px;width:220px;height:98px;background:var(--panel);text-align:center;padding-top:12px;box-shadow:0 8px 8px -6px rgba(0,0,0,.25)}
.panel-title{font-family:"Signika",sans-serif;font-weight:700;font-size:20px;color:#3f3f3f}
.panel-title em{font-style:normal;color:var(--head-green)}
.social{display:flex;gap:9px;justify-content:center;margin-top:12px}
.social span{width:30px;height:30px;border-radius:4px}
.s1{background:#3b5a9a}.s2{background:#59b8e4}.s3{background:#1e6fa0}.s4{background:#f07a1f}.s5{background:#c8221f}

.newsletter{left:371px;top:422px;width:699px;height:98px;background:var(--panel);text-align:center;padding-top:12px;box-shadow:0 8px 8px -6px rgba(0,0,0,.25)}
.news-form{display:flex;gap:10px;margin:12px 0 0 82px}
.news-input{width:404px;height:33px;border:1px solid #bbb;border-radius:5px;background:var(--white)}
.btn{background:linear-gradient(#bcd95a,#97bb36);border:1px solid #7fa02c;border-radius:3px;color:var(--white);font-family:"Signika",sans-serif;font-weight:700;text-shadow:0 1px 1px rgba(0,0,0,.3);display:flex;align-items:center;justify-content:center}
.btn.subscribe{width:122px;height:33px;font-size:16px}

.box{background:#f5f5f5;border:3px solid #ececec}
.welcome{left:130px;top:554px;width:620px;height:320px;padding:12px 22px}
.box h1{font-family:"Signika",sans-serif;font-weight:700;font-size:23px;color:var(--head-green)}
.lead{color:var(--lime-text);font-weight:700;font-size:14px;line-height:21px;margin-top:10px;max-width:560px}
.body-copy{font-size:13.4px;line-height:23px;margin-top:10px;color:#555;max-width:562px;letter-spacing:.15px}
.btn.read{position:absolute;left:22px;bottom:24px;width:101px;height:29px;font-size:15px}

.quote{left:770px;top:554px;width:300px;height:320px;text-align:center;padding:18px 20px}
.quote p{font-size:14px;line-height:24px;margin-top:16px}
.btn.get-quote{position:absolute;left:42px;top:199px;width:212px;height:49px;font-size:18px;font-family:"PT Sans",sans-serif}

.footer{left:0;top:892px;width:1200px;height:89px;background:var(--dark);text-align:center;color:#ddd}
.footer-nav{list-style:none;display:flex;justify-content:center;margin-top:25px;font-size:11px;letter-spacing:.4px}
.footer-nav li+li::before{content:"|";margin:0 14px}
.copyright{font-size:10px;color:#bbb;margin-top:12px;letter-spacing:.4px}
</style>
</head>
<body>
<div class="topbar"></div>

<div class="abs logo"><span class="logo-mark"></span><span class="logo-name">TESSARO<br>LANE</span></div>
<div class="abs tagline">Because You´re Awesome!</div>

<nav class="abs nav">
  <div class="nav-tab active">Tessaro Lane</div>
  <div class="nav-tab">Be Found</div>
  <div class="nav-tab">Connect</div>
  <div class="nav-tab">Get Growing</div>
</nav>

<ul class="abs side-menu">
  <li class="current">STRATEGY</li>
  <li>PORTFOLIO</li>
  <li>ABOUT US</li>
  <li>CONTACT US</li>
  <li>BLOG</li>
</ul>

<section class="abs hero">
  <div class="hero-art" role="img" aria-label="Illustration of a person surrounded by social media bubbles linked by dashed paths to a brand circle and a group of friends"></div>
  <div class="callout">
    <h2>What’s the upside of being ‘social’?</h2>
    <p>Speak to one of our communications strategists now ›</p>
  </div>
</section>

<section class="abs connect">
  <div class="panel-title">CONNECT WITH US</div>
  <div class="social"><span class="s1"></span><span class="s2"></span><span class="s3"></span><span class="s4"></span><span class="s5"></span></div>
</section>

<section class="abs newsletter">
  <div class="panel-title">GET TIPS AND TRICKS! <em>SUBSCRIBE TO OUR NEWSLETTER</em></div>
  <div class="news-form"><div class="news-input"></div><div class="btn subscribe">SUBSCRIBE</div></div>
</section>

<section class="abs box welcome">
  <h1>Welcome to Our Site</h1>
  <p class="lead">Lorem ipsum dolor sit amet, consectetur adipiscing elit. Fusce accumsan, elit a suscipit sagittis, tortor sapien cursus risus, non rhoncus lectus nunc ac nulla..</p>
  <p class="body-copy">Aliquam molestie, mi et imperdiet euismod, dui purus auctor tellus, et interdum lacus lectus et ante. Sed accumsan sollicitudin sapien, sit amet adipiscing turpis gravida ac. In congue, neque ac lobortis volutpat, libero mauris varius mi, vitae suscipit ipsum ligula vitae risus. Duis aliquam nibh a dui iaculis viverra id a velit. Vivamus egestas risus in magna varius commodo. Sed semper viverra egestas. Etiam pretium porttitor lectus, vel ornare neque porta volutpat. Aenean a nibh eget turpis vehicula tempus ac sed massa.</p>
  <div class="btn read">Read More</div>
</section>

<section class="abs box quote">
  <h1>Get a Free Quote</h1>
  <p>If you would like to more information on how we can help you achive your goals. You can visit our strategy page or simply get a free Quote !</p>
  <div class="btn get-quote">GET A FREE QUOTE</div>
</section>

<footer class="abs footer">
  <ul class="footer-nav"><li>STRATEGY</li><li>PORTFOLIO</li><li>ABOUT US</li><li>CONTACT US</li><li>BLOG</li><li>SITE MAP</li></ul>
  <p class="copyright">COPYRIGHT ©2013. TESSARO LANE INC. | ALL RIGHT RESERVED</p>
</footer>
</body>
</html>
```